Website for courses for men for making money, health, fitness

I require a website which is going to be a mix of a crypto currency website and website aimed at providing men with money making, health, relationship advice courses and content

The name isn't decided yet so for now please call it something like

MAVERLY DEN

A platform dedicated to making men wealthy, physically strong, mentally tough & successful with women

In the top right, I need it to show how many points they have, they must buy points in order to use them to claim the courses.

WHAT WE DO

Maverly den is a platform where you can learn everything you need about business, making money, crypto currency, fitness, health, mental toughness and resilience and how to be successful with women all in one place

HOW WILL THIS WORK & WHY SHOULD I BUY POINTS?

xxxxxxxxxxxxxxxxxxxxxxxx
xxxxxxxxxxxxxxxxxxxxxxx
xxxxxxxxxxxxxxxxxxxxx

AFFILIATE SCHEME

EARN UP TO $125 DOLLARS PER PERSON WHO SIGNS UP THROUGH YOUR LINK

START EARNING NOW - button
______________________________________________________

BUY POINTS
(A maximum of only $250 worth of points can be purchased per person until the platform goes fully live)

ROAD MAP & THE MODEL

2023

Q1 - PRE BUY IN FOR POINTS

Q2 - FULL WEBSITE LAUNCH

Q3 - APP LAUNCH

Q4 - IN APP ADVERT LAUNCH

It must have a very slick and sharp eye catching look, and be designed to convert people into purchasing points

some ideas of the feel of the website -

https://trendlumo.io/
https://velmora.style/
https://plume.quorvix.com/

```html
<!DOCTYPE html>
<html lang="en">
<head>
<meta charset="utf-8">
<title>MAVERLY DEN</title>
<link rel="stylesheet" href="https://fonts.googleapis.com/css2?family=Oswald:wght@500;600&family=Roboto:wght@400;500;700&display=swap">
<style>
:root{
  --navy:#1c2130;
  --navy-deep:#171b27;
  --navy-soft:#222838;
  --orange:#f0952f;
  --orange-dark:#d97f1c;
  --white:#ffffff;
  --ink:#1d1d1d;
  --grey:#777b84;
  --line:#e9e9e9;
}
*{margin:0;padding:0;box-sizing:border-box}
html,body{width:1200px;height:3676px;overflow:hidden}
body{position:relative;background:var(--navy);font-family:'Roboto',sans-serif;color:var(--white)}
.abs{position:absolute}
.display{font-family:'Oswald',sans-serif;font-weight:500;text-transform:uppercase;letter-spacing:0}
.btn{position:absolute;display:flex;align-items:center;justify-content:center;font-family:'Roboto',sans-serif;font-weight:700;font-size:13px;text-transform:uppercase;text-decoration:none}
.btn-orange{background:var(--orange);color:var(--white)}
.btn-white{background:var(--white);color:var(--ink)}
.rule{position:absolute;height:4px;background:var(--orange)}

/* header */
.site-header{position:absolute;left:0;top:0;width:1200px;height:116px;background:var(--navy-deep)}
.brand{left:110px;top:34px;font-size:38px;color:var(--white)}
.main-nav{left:392px;top:52px;display:flex;gap:19px;font-size:12.5px;font-weight:700}
.main-nav .is-active{color:var(--orange)}
.points-balance{left:936px;top:39px;width:153px;height:42px;font-weight:700;font-size:13px}

/* hero */
.hero{position:absolute;left:0;top:116px;width:1200px;height:617px;background:linear-gradient(100deg,#1d2233 0%,#202739 55%,#1a2a3c 100%)}
.hero-art{left:170px;top:90px;width:380px;height:445px;border-radius:50%;background:radial-gradient(circle at 50% 50%,#6b4a2c 0%,#3a3434 45%,rgba(32,39,57,0) 72%)}
.hero-data{left:960px;top:0;width:240px;height:617px;background:linear-gradient(90deg,rgba(32,39,57,0),rgba(36,92,120,.45))}
.hero-title{left:596px;top:210px;font-size:66px;line-height:1}
.hero-lead{left:596px;top:300px;width:420px;font-size:20px;line-height:31px}

/* what we do */
.about{position:absolute;left:0;top:733px;width:1200px;height:560px;background:var(--navy)}
.about-art{left:740px;top:0;width:460px;height:560px;background:radial-gradient(circle at 55% 45%,#2f6f92 0%,#1f3b55 38%,rgba(28,33,48,0) 70%)}
.about-title{left:112px;top:130px;font-size:72px;line-height:1}
.about-title-rule{left:112px;top:197px;width:162px;height:10px}
.about-text{left:112px;top:245px;width:497px;font-size:17px;line-height:29px;text-align:justify;color:#e6e7ea}
.about .btn{left:112px;top:397px;width:120px;height:42px}

/* how it works */
.how{position:absolute;left:0;top:1293px;width:1200px;height:642px;background:var(--orange)}
.how-title{left:0;top:80px;width:1200px;text-align:center;font-size:43px;line-height:54px}
.how-rule{left:544px;top:196px;width:112px}
.card{position:absolute;top:250px;width:307px;height:298px;background:var(--white);border:3px solid #2a2a2a;border-radius:4px;text-align:center;color:var(--ink)}
.card-icon{position:absolute;left:111px;top:40px;width:84px;height:84px}
.card-title{position:absolute;left:0;top:155px;width:100%;font-size:16px;font-weight:700}
.card-text{position:absolute;left:8px;top:190px;width:285px;font-size:13.5px;line-height:24px;color:var(--grey)}

/* affiliate */
.affiliate{position:absolute;left:0;top:1935px;width:1200px;height:395px;background:var(--navy)}
.affiliate-art{left:0;top:150px;width:1200px;height:245px;background:linear-gradient(170deg,rgba(28,33,48,0) 10%,rgba(38,104,118,.45) 45%,rgba(28,33,48,0) 85%)}
.affiliate-title{left:0;top:96px;width:1200px;text-align:center;font-size:52px;line-height:1}
.affiliate-rule{left:544px;top:166px;width:112px}
.affiliate-text{left:0;top:202px;width:1200px;text-align:center;font-size:18px;font-weight:500;color:#e8e9ec}
.affiliate .btn{left:510px;top:257px;width:180px;height:42px}

/* buy points */
.buy{position:absolute;left:0;top:2330px;width:1200px;height:283px;background:var(--orange)}
.buy-title{left:188px;top:52px;font-size:72px;line-height:1}
.buy-title-rule{left:188px;top:118px;width:154px;height:10px;background:var(--navy-deep)}
.buy-text{left:188px;top:165px;width:560px;font-size:17px;line-height:29px;font-weight:500}
.buy .btn{left:893px;top:121px;width:119px;height:41px;font-weight:500}

/* roadmap */
.roadmap{position:absolute;left:0;top:2613px;width:1200px;height:735px;background:var(--navy)}
.roadmap-title{left:0;top:92px;width:1200px;text-align:center;font-size:52px;line-height:1}
.roadmap-rule{left:544px;top:160px;width:112px}
.roadmap-lines{left:0;top:0}
.year{left:121px;top:348px;width:244px;height:244px;border-radius:50%;border:7px solid var(--white);background:radial-gradient(circle at 40% 40%,#f3a142,#c9761d);display:flex;align-items:center;justify-content:center;font-size:64px}
.quarter{position:absolute;width:84px;height:84px;border-radius:50%;border:5px solid var(--white);background:var(--navy);display:flex;align-items:center;justify-content:center;color:var(--orange);font-size:30px}
.quarter-label{position:absolute;font-size:20px;font-weight:500;text-transform:uppercase}

/* footer */
.site-footer{position:absolute;left:0;top:3348px;width:1200px;height:328px;background:var(--navy-deep)}
.footer-brand{left:0;top:50px;width:1200px;text-align:center;font-size:40px;line-height:1}
.footer-nav{left:0;width:1200px;display:flex;justify-content:center;gap:22px;font-size:16px;font-weight:700}
.footer-nav span.sep{font-weight:400}
.socials{left:520px;top:208px;display:flex;gap:7px}
.social{width:35px;height:35px;border-radius:50%;background:var(--white)}
.social.is-first{background:var(--orange)}
.footer-divider{left:110px;top:266px;width:980px;height:1px;background:#2f3546}
.copyright{left:0;top:289px;width:1200px;text-align:center;font-size:12px}
.copyright b{font-weight:700}
</style>
</head>
<body>

<header class="site-header">
  <div class="abs brand display">MAVERLY DEN</div>
  <nav class="abs main-nav">
    <span class="is-active">HOME</span><span>ABOUT</span><span>HOW IT WORKS</span><span>WHAT WE DO</span><span>BLOG</span>
  </nav>
  <a class="btn btn-orange" style="left:816px;top:39px;width:120px;height:42px;font-weight:500">Buy Points</a>
  <div class="btn btn-white points-balance">1 POINTS = $250</div>
</header>

<section class="hero">
  <div class="abs hero-art" role="img" aria-label="Glowing digital coin illustration in copper and blue light"></div>
  <div class="abs hero-data" role="img" aria-label="Blurred lines of code on a dark blue background"></div>
  <h1 class="abs hero-title display">MAVERLY DEN</h1>
  <p class="abs hero-lead">A platform dedicated to making men wealthy, physically strong, mentally tough &amp; successful with women.</p>
</section>

<section class="about">
  <div class="abs about-art" role="img" aria-label="Glowing blue digital coin within a network of connected dots"></div>
  <div class="abs rule about-title-rule"></div>
  <h2 class="abs about-title display">WHAT WE DO</h2>
  <p class="abs about-text">Maverly den is a platform where you can learn everything you need about business, making money, crypto currency, fitness, health, mental toughness and resilience and how to be successful with women all in one place</p>
  <a class="btn btn-orange">Learn More</a>
</section>

<section class="how">
  <h2 class="abs how-title display">HOW WILL THIS WORK &amp;<br>WHY SHOULD I BUY POINTS?</h2>
  <div class="rule how-rule"></div>

  <article class="card" style="left:112px">
    <svg class="card-icon" viewBox="0 0 84 84"><circle cx="42" cy="42" r="42" fill="#f0952f"/><circle cx="36" cy="46" r="14" fill="none" stroke="#fff" stroke-width="2.5"/><circle cx="49" cy="36" r="12" fill="none" stroke="#fff" stroke-width="2.5"/><text x="36" y="52" font-family="Roboto,sans-serif" font-size="16" font-weight="700" fill="#fff" text-anchor="middle">$</text></svg>
    <h3 class="card-title">LOREM IPSUM DOLOR</h3>
    <p class="card-text">Lorem ipsum dolor sit amet, consectetur adi piscing elit sed do eiusmod tempor incidi dunt ut labore et dolorea.</p>
  </article>
  <article class="card" style="left:446px">
    <svg class="card-icon" viewBox="0 0 84 84"><circle cx="42" cy="42" r="42" fill="#f0952f"/><path d="M22 58h40l-8-10H30z" fill="none" stroke="#fff" stroke-width="2.5"/><path d="M38 44l16-18M48 24l8 8" stroke="#fff" stroke-width="2.5" fill="none"/></svg>
    <h3 class="card-title">LOREM IPSUM DOLOR</h3>
    <p class="card-text">Lorem ipsum dolor sit amet, consectetur adi piscing elit sed do eiusmod tempor incidi dunt ut labore et dolorea.</p>
  </article>
  <article class="card" style="left:781px">
    <svg class="card-icon" viewBox="0 0 84 84"><circle cx="42" cy="42" r="42" fill="#f0952f"/><circle cx="44" cy="34" r="10" fill="none" stroke="#fff" stroke-width="2.5"/><text x="44" y="39" font-family="Roboto,sans-serif" font-size="13" font-weight="700" fill="#fff" text-anchor="middle">$</text><path d="M20 52h12l8 4h14l8-6" fill="none" stroke="#fff" stroke-width="2.5"/></svg>
    <h3 class="card-title">LOREM IPSUM DOLOR</h3>
    <p class="card-text">Lorem ipsum dolor sit amet, consectetur adi piscing elit sed do eiusmod tempor incidi dunt ut labore et dolorea.</p>
  </article>
</section>

<section class="affiliate">
  <div class="abs affiliate-art" role="img" aria-label="Teal glowing data network stream across a dark background"></div>
  <h2 class="abs affiliate-title display">AFFILIATE SCHEME</h2>
  <div class="rule affiliate-rule"></div>
  <p class="abs affiliate-text">EARN UP TO $125 DOLLARS PER PERSON WHO SIGNS UP THROUGH YOUR LINK</p>
  <a class="btn btn-orange">Start Earning Now</a>
</section>

<section class="buy">
  <div class="abs buy-title-rule"></div>
  <h2 class="abs buy-title display">BUY POINTS</h2>
  <p class="abs buy-text">A maximum of only $250 worth of points can be purchased per person until the platform goes fully live</p>
  <a class="btn btn-white">Buy Points</a>
</section>

<section class="roadmap">
  <h2 class="abs roadmap-title display">ROAD MAP &amp; THE MODEL</h2>
  <div class="rule roadmap-rule"></div>
  <svg class="abs roadmap-lines" width="1200" height="735" viewBox="0 0 1200 735" fill="none" stroke="#fff" stroke-width="2">
    <path d="M357 424H460L535 258H650"/>
    <path d="M498 476L545 357H735"/>
    <path d="M533 532L502 474L535 415L556 419"/>
    <path d="M533 532H580L556 419"/>
    <path d="M568 532H740"/>
    <path d="M364 519H471L507 605H642"/>
    <circle cx="650" cy="258" r="6" fill="#1c2130"/>
    <circle cx="735" cy="357" r="6" fill="#1c2130"/>
    <circle cx="740" cy="532" r="6" fill="#1c2130"/>
    <circle cx="642" cy="605" r="6" fill="#1c2130"/>
    <circle cx="556" cy="419" r="6" fill="#1c2130"/>
    <circle cx="533" cy="532" r="6" fill="#1c2130"/>
  </svg>
  <div class="abs year display" role="img" aria-label="2023 badge over an orange-toned photo of a desk">2023</div>

  <div class="quarter display" style="left:656px;top:215px">Q1</div>
  <div class="quarter-label" style="left:773px;top:244px">Pre Buy In For Points</div>
  <div class="quarter display" style="left:743px;top:315px">Q2</div>
  <div class="quarter-label" style="left:860px;top:344px">Full Website Launch</div>
  <div class="quarter display" style="left:749px;top:490px">Q3</div>
  <div class="quarter-label" style="left:866px;top:519px">App Launch</div>
  <div class="quarter display" style="left:650px;top:561px">Q4</div>
  <div class="quarter-label" style="left:768px;top:590px">In App Advert Launch</div>
</section>

<footer class="site-footer">
  <div class="abs footer-brand display">MAVERLY DEN</div>
  <nav class="abs footer-nav" style="top:124px">
    <span>HOME</span><span class="sep">/</span><span>ABOUT</span><span class="sep">/</span><span>HOW IT WORKS</span><span class="sep">/</span><span>WHAT WE DO</span><span class="sep">/</span><span>BLOG</span><span class="sep">/</span><span>BUY POINTS</span>
  </nav>
  <nav class="abs footer-nav" style="top:163px">
    <span>PRIVACY POLICY</span><span class="sep">/</span><span>TERMS OF USE</span><span class="sep">/</span><span>DISCLAIMER</span>
  </nav>
  <div class="abs socials">
    <span class="social is-first" aria-label="Social link"></span>
    <span class="social" aria-label="Social link"></span>
    <span class="social" aria-label="Social link"></span>
    <span class="social" aria-label="Social link"></span>
  </div>
  <div class="abs footer-divider"></div>
  <p class="abs copyright">© 2022 <b>MAVERLY DEN</b> | &nbsp;All Rights Reserved</p>
</footer>

</body>
</html>
```